Sheriff Candidate needs a large yard sign

A candidate for Sheriff needs to have a sign to put in front of businesses and houses that advertise her candidacy.

Target Market(s)

Democrats, voters

Industry/Entity Type

Political

Font styles to use
Sans Serif

Colors
34a7d7
3276b5

Requirements
Must have
• Must have her picture
• Must have the words "Elect Dana Whitlock" - I'd like the name Dana to be smaller Whitlock. "Elect" and "Whitlock" should be the focus.
• at the bottom in a box "Paid for by the Committee to Elect Dana Whitlock"
Nice to have
• it would be good to have her logo as well.
• blue color for democrats and on a white background
Should not have
• pink color

```html
<!DOCTYPE html>
<html lang="en">
<head>
<meta charset="utf-8">
<title>Elect Dana Whitlock – Yard Sign</title>
<link rel="stylesheet" href="https://fonts.googleapis.com/css2?family=Archivo+Black&family=Oswald:wght@700&family=Open+Sans:wght@400;800&display=swap">
<style>
  :root {
    --royal-blue: #3276b5;
    --sky-blue: #34a7d7;
    --white: #ffffff;
    --paper: #ececec;
    --ink: #111418;
    --gold: #c9a23a;
    --navy: #1c2434;
  }
  html, body {
    margin: 0;
    padding: 0;
    width: 1200px;
    height: 880px;
    overflow: hidden;
    background: var(--white);
  }
  .yard-sign {
    position: relative;
    width: 1200px;
    height: 880px;
    background: var(--royal-blue);
    overflow: hidden;
  }
  .wave-backdrop {
    position: absolute;
    inset: 0;
  }
  .headline {
    position: absolute;
    left: 0;
    top: 0;
  }
  .headline-elect {
    font-family: "Archivo Black", "Arial Black", sans-serif;
  }
  .headline-name {
    font-family: "Oswald", "Arial Narrow", sans-serif;
    font-weight: 700;
  }
  .headline .letter-fill { fill: var(--white); }
  .headline .letter-shadow { fill: var(--ink); }
  .campaign-mark {
    position: absolute;
    left: 265px;
    top: 468px;
    width: 244px;
    height: 244px;
    border-radius: 50%;
    background: var(--gold);
    display: flex;
    align-items: center;
    justify-content: center;
    text-align: center;
  }
  .campaign-mark-name {
    font-family: "Open Sans", sans-serif;
    font-weight: 800;
    font-size: 30px;
    line-height: 1.1;
    color: var(--navy);
    text-transform: uppercase;
    letter-spacing: 1px;
  }
  .candidate-portrait {
    position: absolute;
    left: 786px;
    top: 21px;
    width: 414px;
    height: 768px;
    border-radius: 180px 180px 0 0;
    background: linear-gradient(180deg, #7a5a44 0%, #c89c82 22%, #2a3142 42%, #1c2434 100%);
  }
  .disclaimer-band {
    position: absolute;
    left: 0;
    top: 789px;
    width: 1200px;
    height: 91px;
    background: var(--royal-blue);
    display: flex;
    align-items: center;
    justify-content: center;
    font-family: "Open Sans", sans-serif;
    font-size: 35px;
    color: var(--white);
    text-transform: uppercase;
    white-space: nowrap;
  }
  .disclaimer-band strong {
    font-weight: 800;
    margin-left: 10px;
  }
</style>
</head>
<body>
<main class="yard-sign">
  <svg class="wave-backdrop" width="1200" height="880" viewBox="0 0 1200 880" aria-hidden="true">
    <defs>
      <linearGradient id="paper-fade" x1="0" y1="0" x2="0" y2="1">
        <stop offset="0" stop-color="#ffffff"/>
        <stop offset="1" stop-color="#ececec"/>
      </linearGradient>
    </defs>
    <path class="wave-sky" fill="#34a7d7" d="M0,377 C150,480 260,560 400,570 C560,580 720,420 1200,300 L1200,880 L0,880 Z"/>
    <path class="wave-paper" fill="url(#paper-fade)" d="M0,498 C120,600 240,675 360,675 C560,675 760,420 1200,325 L1200,880 L0,880 Z"/>
  </svg>

  <svg class="headline" width="800" height="440" viewBox="0 0 800 440">
    <title>Elect Dana Whitlock</title>
    <g class="headline-elect" font-size="212">
      <text class="letter-shadow" x="76" y="244" textLength="490" lengthAdjust="spacingAndGlyphs">ELECT</text>
      <text class="letter-fill" x="70" y="238" textLength="490" lengthAdjust="spacingAndGlyphs">ELECT</text>
    </g>
    <g class="headline-name">
      <text class="letter-shadow" x="76" y="409" font-size="128" textLength="190" lengthAdjust="spacingAndGlyphs">DANA</text>
      <text class="letter-fill" x="70" y="403" font-size="128" textLength="190" lengthAdjust="spacingAndGlyphs">DANA</text>
      <text class="letter-shadow" x="290" y="409" font-size="172" textLength="490" lengthAdjust="spacingAndGlyphs">WHITLOCK</text>
      <text class="letter-fill" x="284" y="403" font-size="172" textLength="490" lengthAdjust="spacingAndGlyphs">WHITLOCK</text>
    </g>
  </svg>

  <div class="campaign-mark">
    <span class="campaign-mark-name">Whitlock<br>for Sheriff</span>
  </div>

  <div class="candidate-portrait" role="img" aria-label="Portrait photograph of candidate Dana Whitlock in a dark blazer, smiling"></div>

  <footer class="disclaimer-band">
    Paid for by the Committee to <strong>Elect Dana Whitlock</strong>
  </footer>
</main>
</body>
</html>
```